Flyer design for commercial marketing

Looking to get a flyer design to email out to companies indicating our services
Company Name - Brightwell Networks
Company Logo - (Attached)
Services Offered
FULL HD DIGITAL IP CCTV SYSTEMS
IP ACCESS CONTROL SYSTEMS RFID / BIOMETRIC
IP EMPLOYEE MANAGEMENT SYSTEMS RFID / BIOMETRIC
NETWORKING / FIBER OPTIC SOLUTIONS
The designer can input necessary text and images
It is up to the designer to put images. I dont want the flyer too tacky. I am using this for commercial advertising
Updates
Target Market(s)
Corporate
Industry/Entity Type
It Company
Look and feel
Each slider illustrates characteristics of the customer's brand and the style your logo design should communicate.

```html
<!DOCTYPE html>
<html lang="en">
<head>
<meta charset="utf-8">
<title>Brightwell Networks — Services Flyer</title>
<link href="https://fonts.googleapis.com/css2?family=Oswald:wght@500;600&family=Open+Sans:wght@400;600;700&display=swap" rel="stylesheet">
<style>
  :root {
    --navy: #0a1f3d;
    --deep-blue: #0d3c78;
    --brand-blue: #1a73c9;
    --sky-blue: #3fa3e8;
    --glow-blue: #7cc8f5;
    --brand-red: #c4161c;
    --dark-red: #7d0d12;
    --ink: #1d2330;
    --white: #ffffff;
    --paper: #eef1f5;
  }
  html, body { margin: 0; padding: 0; overflow: hidden; background: var(--paper); }
  .flyer {
    position: relative; width: 900px; height: 1200px; overflow: hidden;
    background: var(--white); font-family: "Open Sans", Arial, sans-serif; color: var(--ink);
  }
  .hero-photo {
    position: absolute; left: 0; top: 0; width: 900px; height: 730px;
    background:
      radial-gradient(ellipse 260px 200px at 640px 330px, rgba(124,200,245,0.85) 0%, rgba(124,200,245,0) 100%),
      radial-gradient(ellipse 420px 300px at 430px 180px, rgba(63,163,232,0.55) 0%, rgba(63,163,232,0) 100%),
      radial-gradient(ellipse 380px 260px at 820px 520px, rgba(26,115,201,0.6) 0%, rgba(26,115,201,0) 100%),
      linear-gradient(160deg, #0b2a55 0%, #0d3c78 40%, #0a2448 75%, #071a36 100%);
  }
  .corner-bands { position: absolute; left: 0; top: 0; }
  .camera-photo {
    position: absolute; left: 0; top: 300px; width: 330px; height: 230px;
    background: radial-gradient(ellipse 170px 100px at 140px 115px, #f6f8fa 0%, #d3d9df 55%, rgba(190,199,208,0) 100%);
  }
  .hero-curve { position: absolute; left: 0; top: 470px; }
  .headline-band {
    position: absolute; left: 290px; top: 560px; width: 610px; height: 66px;
    background: linear-gradient(90deg, var(--dark-red), var(--brand-red) 30%);
    clip-path: polygon(30px 0, 100% 0, 100% 100%, 0 100%);
  }
  .headline {
    position: absolute; left: 330px; top: 568px; margin: 0;
    font-family: "Oswald", Arial, sans-serif; font-weight: 600; font-size: 38px;
    color: var(--white); letter-spacing: 0.5px; text-transform: uppercase; line-height: 50px;
  }
  .intro-block {
    position: absolute; left: 290px; top: 626px; width: 610px; height: 104px;
    background: linear-gradient(90deg, rgba(125,13,18,0.9), rgba(10,31,61,0.92));
  }
  .intro-text {
    position: absolute; left: 330px; top: 636px; width: 545px; margin: 0;
    font-size: 14px; line-height: 21px; color: var(--white);
  }
  .brand {
    position: absolute; left: 40px; top: 860px; display: flex; align-items: center; gap: 18px;
  }
  .brand-dot { width: 70px; height: 70px; border-radius: 50%; background: var(--brand-blue); }
  .brand-name {
    font-family: "Oswald", Arial, sans-serif; font-weight: 600; font-size: 38px;
    line-height: 44px; color: var(--deep-blue); letter-spacing: 2px; text-transform: uppercase;
  }
  .services { position: absolute; left: 420px; top: 756px; width: 460px; }
  .services-title {
    margin: 0 0 10px; font-family: "Oswald", Arial, sans-serif; font-weight: 600;
    font-size: 32px; color: var(--brand-red); text-transform: uppercase;
  }
  .services-list { margin: 0; padding: 0; list-style: none; }
  .services-list li {
    position: relative; padding-left: 22px; font-size: 18px; font-weight: 700;
    line-height: 29px; color: var(--ink);
  }
  .services-list li::before {
    content: ""; position: absolute; left: 0; top: 10px; width: 9px; height: 9px;
    background: var(--brand-red); border-radius: 50%;
  }
  .device-photo {
    position: absolute; left: 700px; top: 965px; width: 180px; height: 165px;
    background: radial-gradient(ellipse 100px 90px at 90px 80px, #5a6069 0%, #2a2e35 60%, #15181d 100%);
    border-radius: 12px;
  }
  .footer-band { position: absolute; left: 0; top: 1040px; }
  .call {
    position: absolute; left: 40px; top: 1082px; color: var(--white);
    font-family: "Oswald", Arial, sans-serif; font-weight: 500; text-transform: uppercase;
  }
  .call-label { font-size: 32px; line-height: 38px; display: block; }
  .call-number { font-size: 40px; line-height: 50px; display: block; }
  .contact-list { position: absolute; left: 330px; top: 1090px; margin: 0; padding: 0; list-style: none; }
  .contact-list li {
    display: flex; align-items: center; gap: 12px; font-size: 19px; color: var(--white);
    line-height: 42px;
  }
</style>
</head>
<body>
<div class="flyer">
  <div class="hero-photo" role="img" aria-label="Hand reaching toward a glowing digital network interface in blue light"></div>

  <svg class="corner-bands" width="900" height="200" viewBox="0 0 900 200" aria-hidden="true">
    <polygon points="0,0 420,0 0,150" fill="#1a73c9"/>
    <polygon points="0,0 300,0 0,100" fill="#3fa3e8"/>
    <polygon points="0,0 170,0 0,55" fill="#0d3c78"/>
    <polygon points="540,0 900,0 900,18 570,18" fill="#3fa3e8"/>
    <polygon points="600,18 900,18 900,26 612,26" fill="#1a73c9"/>
  </svg>

  <svg class="hero-curve" width="900" height="260" viewBox="0 0 900 260" aria-hidden="true">
    <path d="M0,60 C120,110 230,150 290,150 L290,260 L0,260 Z" fill="#ffffff"/>
    <path d="M0,40 C120,95 230,135 290,140 L290,150 C230,150 120,110 0,60 Z" fill="#c4161c"/>
  </svg>

  <div class="camera-photo" role="img" aria-label="White bullet-style CCTV security camera"></div>

  <div class="headline-band"></div>
  <h1 class="headline">Smart security for business</h1>
  <div class="intro-block"></div>
  <p class="intro-text">Brightwell Networks designs, installs and supports complete IP security and network infrastructure for corporate sites. From full HD surveillance to biometric access and fibre backbones, we deliver reliable systems that protect your people, assets and data.</p>

  <div class="brand">
    <div class="brand-dot"></div>
    <div class="brand-name">Brightwell<br>Networks</div>
  </div>

  <section class="services">
    <h2 class="services-title">Services Offered</h2>
    <ul class="services-list">
      <li>Full HD digital IP CCTV systems</li>
      <li>IP access control systems RFID</li>
      <li>Biometric</li>
      <li>IP employee management systems RFID</li>
      <li>Biometric</li>
      <li>Networking</li>
      <li>Fiber optic solutions</li>
    </ul>
  </section>

  <svg class="footer-band" width="900" height="160" viewBox="0 0 900 160" aria-hidden="true">
    <polygon points="0,20 640,20 680,0 900,0 900,160 0,160" fill="#0d3c78"/>
    <polygon points="0,30 300,30 270,160 0,160" fill="#1a73c9"/>
    <polygon points="0,20 640,20 636,30 0,30" fill="#c4161c"/>
  </svg>

  <div class="device-photo" role="img" aria-label="Biometric fingerprint access terminal with keypad"></div>

  <div class="call">
    <span class="call-label">Call us now</span>
    <span class="call-number">+6495550182</span>
  </div>

  <ul class="contact-list">
    <li>
      <svg width="26" height="26" viewBox="0 0 26 26" aria-hidden="true">
        <circle cx="13" cy="13" r="11" fill="none" stroke="#ffffff" stroke-width="2"/>
        <ellipse cx="13" cy="13" rx="5" ry="11" fill="none" stroke="#ffffff" stroke-width="1.6"/>
        <line x1="2" y1="13" x2="24" y2="13" stroke="#ffffff" stroke-width="1.6"/>
      </svg>
      www.brightwellnet.com
    </li>
    <li>
      <svg width="26" height="26" viewBox="0 0 26 26" aria-hidden="true">
        <rect x="2" y="6" width="22" height="15" rx="2" fill="none" stroke="#ffffff" stroke-width="2"/>
        <polyline points="3,7 13,15 23,7" fill="none" stroke="#ffffff" stroke-width="2"/>
      </svg>
      info@brightwellnet.com
    </li>
  </ul>
</div>
</body>
</html>
```